B2B telecom company need web design

We need a web design for our corporate web site. The company exists since almost 10 years.
This is a DESIGN contest, you're expected to provide design only, NOT the whole website. The winner will have to provide the HTML template (with Lorem Ipsum content) and the CSS files of his design.
Our initial product is SMS peering in P2P (you send a SMS to a friend in a foreign country, great chance that your operator route your SMS to us that we route to the recipient). We're launching a bulk SMS service (marketing and application to SMS).
Target is mostly corporate, usually big corporate (operators, contents providers...) where use of SMS is part of the main business.
The web site is composed of 1 landing page and 7 content pages (plan is given for your information, all content page are using the same template and the same design, you do NOT need to make one design per page) :
* About US
Company Profile
They trust us
The Vortel Team
Partners
Contact us
* Solution
P2P SMS
A2P SMS
You only need to submit the landing page and a template page for the content (with h1, h2, h3 and h4).
Design must be based on our new logo (see attached file).
Our current web site http://www.vortel-example.com
The winner of the contest will have to provide state of the art HTML template and CSS files of his design. Photo used shall be downloaded from Pixaldo (provide the ID of the picture that we purchase file).
Target Market(s)
Telecom operator. SMS Peering hubs. Bulk SMS.
Industry/Entity Type
It Company
Number of Pages Required
2 page
Look and feel

```html
<!DOCTYPE html>
<html lang="en">
<head>
<meta charset="utf-8">
<title>Vortel mobile</title>
<link rel="stylesheet" href="https://fonts.googleapis.com/css2?family=Open+Sans:wght@300;400;600;700&display=swap">
<style>
:root{
  --green:#7ab929;
  --green-dark:#5f9a17;
  --ink:#222;
  --muted:#777;
  --light:#f2f2f2;
  --grey:#e6e6e6;
  --field:#d3d3d3;
  --white:#fff;
}
*{box-sizing:border-box;margin:0;padding:0}
html,body{width:1200px;height:3770px;overflow:hidden}
body{font-family:"Open Sans",Arial,sans-serif;color:var(--ink);background:var(--white);position:relative}
section,header,footer{position:absolute;left:0;width:1200px}
.abs{position:absolute}

/* header */
.site-header{top:0;height:88px;background:var(--white)}
.brand{left:44px;top:24px;font-size:32px;font-weight:400;color:var(--ink)}
.menu-btn{right:44px;top:30px;width:26px;height:26px;border:3px solid var(--ink);border-radius:5px;padding:4px 3px}
.menu-btn i{display:block;height:2px;background:var(--ink);margin:2px 0}

/* hero */
.hero{top:88px;height:682px;background:linear-gradient(100deg,#6c6a66 0%,#a79785 35%,#c8a78a 60%,#8d7a66 100%)}
.hero-band{left:0;bottom:0;width:100%;height:120px;background:linear-gradient(rgba(0,0,0,0),rgba(0,0,0,.35))}
.hero-kicker{left:76px;top:562px;font-size:18px;color:var(--white)}
.hero-title{left:76px;top:594px;font-size:46px;font-weight:300;color:var(--white);white-space:nowrap}
.btn{display:flex;align-items:center;justify-content:center;background:var(--green);color:var(--white);font-weight:600;text-transform:uppercase;border-radius:3px;box-shadow:0 3px 0 var(--green-dark)}
.hero-btn{left:951px;top:609px;width:173px;height:54px;font-size:17px}

/* expectations */
.expect{top:770px;height:885px;background:var(--white);text-align:center}
.section-title{font-size:38px;font-weight:400;color:var(--ink)}
.expect .section-title{position:absolute;top:90px;width:100%}
.expect-sub{position:absolute;top:160px;width:100%;font-size:24px;font-weight:300;color:var(--muted)}
.expect-copy{position:absolute;left:141px;top:210px;width:918px;font-size:15.5px;line-height:24px;color:var(--muted)}
.service-card{left:110px;width:958px;height:198px;background:var(--white);box-shadow:0 6px 14px rgba(0,0,0,.18);text-align:left}
.service-icon{left:55px;top:44px;width:100px;height:100px;border:2px solid #999;border-radius:50%}
.service-card h3{position:absolute;left:226px;top:30px;font-size:22px;font-weight:700}
.service-card p{position:absolute;left:226px;top:70px;width:700px;font-size:15.5px;line-height:25px;color:#444}

/* security */
.security{top:1655px;height:710px;background:var(--light)}
.security .section-title{position:absolute;top:70px;width:100%;text-align:center;line-height:52px}
.features-label{left:148px;top:210px;font-size:22px;color:var(--muted)}
.features{left:146px;top:260px;list-style:none}
.features li{font-size:16px;color:#555;height:49px;display:flex;align-items:center;gap:26px}
.features li svg{flex:none}
.person-photo{left:738px;top:223px;width:345px;height:462px;border-radius:40% 40% 12% 12%;background:linear-gradient(#a0463f,#e8e2dc 40%,#3b4a7a 80%,#e8e8e8)}

/* video */
.video{top:2365px;height:508px;background:linear-gradient(90deg,#3a3a3a,#161616 60%,#050505)}
.video-title{left:110px;top:105px;font-size:36px;font-weight:400;line-height:44px;color:var(--white)}
.video-copy{left:110px;top:212px;width:400px;font-size:15.5px;line-height:24px;color:#ddd}
.video-btn{left:104px;top:335px;width:176px;height:54px;font-size:16px}
.video-frame{left:600px;top:94px;width:518px;height:367px;background:linear-gradient(135deg,#8e7464,#4d5a66 50%,#2d4a5c)}
.video-bar{left:0;bottom:0;width:100%;height:34px;background:#111}

/* partners */
.partners{top:2873px;height:204px;background:var(--white)}
.partner-mark{top:78px;height:50px;background:#d9d9d9;border-radius:6px}

/* contact */
.contact{top:3077px;height:471px;background:var(--grey)}
.contact .section-title{position:absolute;top:90px;width:100%;text-align:center;font-weight:300}
.field{background:var(--field);font-size:14px;color:#333;padding:12px 10px}
.submit-btn{left:490px;top:346px;width:257px;height:50px;font-size:13px;box-shadow:none}

/* footer */
.site-footer{top:3548px;height:222px;background:var(--green);color:var(--white)}
.foot-label{font-size:14px;font-weight:700;text-transform:uppercase;letter-spacing:.5px}
.news-input{left:110px;top:90px;width:228px;height:34px;border-radius:17px;background:var(--white);color:#999;font-size:12px;padding:9px 16px}
.news-go{left:306px;top:94px;width:26px;height:26px;border-radius:50%;background:var(--green)}
.divider{top:48px;width:1px;height:120px;background:rgba(255,255,255,.5)}
.social{left:565px;top:95px;display:flex;gap:12px}
.social i{width:14px;height:14px;border-radius:50%;background:var(--white)}
.foot-brand{left:827px;top:66px;font-size:32px;font-weight:400;color:var(--white)}
.copyright{left:110px;top:162px;font-size:13px}
</style>
</head>
<body>

<header class="site-header">
  <div class="abs brand">Vortel mobile</div>
  <div class="abs menu-btn"><i></i><i></i><i></i></div>
</header>

<section class="hero">
  <div class="abs" role="img" aria-label="Smiling woman using a smartphone, beside a phone showing an SMS app with message envelopes" style="inset:0"></div>
  <div class="abs hero-band"></div>
  <p class="abs hero-kicker">Make Crystal Clear International SMS with Vortel mobile</p>
  <h1 class="abs hero-title">The best way to chat with everyone</h1>
  <a class="abs btn hero-btn">Find out how</a>
</section>

<section class="expect">
  <h2 class="section-title">We Meet your expectations</h2>
  <p class="expect-sub">We Are Competitive in our services</p>
  <p class="expect-copy">Placilisis at vero eros et accumsan et iusto odio dignissim qui bla ndit praesent luptatum zzril delenit augue duis dolore te feugait nulla facilisi. Placilisis at vero eros et accumsan et iusto odio dignissim qui bla ndit praesent luptatum zzril delenit augue duis dolore te feugait nulla facilisi. Placilisis at vero eros et accumsan et iusto odio dignissim qui bla ndit praesent luptatum zzril delenit augue duis dolore te feugait nulla facilisi.</p>

  <article class="abs service-card" style="top:376px">
    <div class="abs service-icon">
      <svg width="96" height="96" viewBox="0 0 96 96" fill="none" stroke="#666" stroke-width="2"><rect x="26" y="30" width="18" height="32" rx="3"/><rect x="52" y="30" width="18" height="32" rx="3"/><path d="M44 40h8M48 36l4 4-4 4"/></svg>
    </div>
    <h3>P2P SMS</h3>
    <p>Lorem ipsum dolor sit amet, consectetur adipiscing elit. Tempora similique excepturi obcaecati, maiores nostrum esse illo in soluta at saepe perspiciatis eos quasi laudantium sunt ad quaeratLorem ipsum dolor sit amet, consectetur adipiscing elit. Tempora similique excepturi</p>
  </article>

  <article class="abs service-card" style="top:627px">
    <div class="abs service-icon">
      <svg width="96" height="96" viewBox="0 0 96 96" fill="none" stroke="#666" stroke-width="2"><rect x="22" y="38" width="30" height="20" rx="2"/><rect x="56" y="32" width="18" height="32" rx="3"/><path d="M65 42v12M62 45h6M62 51h6"/></svg>
    </div>
    <h3>A2P SMS</h3>
    <p>Lorem ipsum dolor sit amet, consectetur adipiscing elit. Tempora similique excepturi obcaecati, maiores nostrum esse illo in soluta at saepe perspiciatis eos quasi laudantium sunt ad quaeratLorem ipsum dolor sit amet, consectetur adipiscing elit. Tempora similique excepturi</p>
  </article>
</section>

<section class="security">
  <h2 class="section-title">We providing Privacy, anonymity and<br>digital&nbsp; security</h2>
  <p class="abs features-label">Amazing features</p>
  <ul class="abs features">
    <li><svg width="14" height="14" viewBox="0 0 14 14"><circle cx="7" cy="7" r="6" fill="none" stroke="#7ab929" stroke-width="1.5"/><path d="M4 7l2 2 4-4" fill="none" stroke="#7ab929" stroke-width="1.5"/></svg>Single connection for global delivery</li>
    <li><svg width="14" height="14" viewBox="0 0 14 14"><circle cx="7" cy="7" r="6" fill="none" stroke="#7ab929" stroke-width="1.5"/><path d="M4 7l2 2 4-4" fill="none" stroke="#7ab929" stroke-width="1.5"/></svg>Intelligent routing engine</li>
    <li><svg width="14" height="14" viewBox="0 0 14 14"><circle cx="7" cy="7" r="6" fill="none" stroke="#7ab929" stroke-width="1.5"/><path d="M4 7l2 2 4-4" fill="none" stroke="#7ab929" stroke-width="1.5"/></svg>Integrated MNP solution</li>
    <li><svg width="14" height="14" viewBox="0 0 14 14"><circle cx="7" cy="7" r="6" fill="none" stroke="#7ab929" stroke-width="1.5"/><path d="M4 7l2 2 4-4" fill="none" stroke="#7ab929" stroke-width="1.5"/></svg>Fraud and Spam control</li>
    <li><svg width="14" height="14" viewBox="0 0 14 14"><circle cx="7" cy="7" r="6" fill="none" stroke="#7ab929" stroke-width="1.5"/><path d="M4 7l2 2 4-4" fill="none" stroke="#7ab929" stroke-width="1.5"/></svg>Credit management and alert</li>
    <li><svg width="14" height="14" viewBox="0 0 14 14"><circle cx="7" cy="7" r="6" fill="none" stroke="#7ab929" stroke-width="1.5"/><path d="M4 7l2 2 4-4" fill="none" stroke="#7ab929" stroke-width="1.5"/></svg>Customer web portal</li>
    <li><svg width="14" height="14" viewBox="0 0 14 14"><circle cx="7" cy="7" r="6" fill="none" stroke="#7ab929" stroke-width="1.5"/><path d="M4 7l2 2 4-4" fill="none" stroke="#7ab929" stroke-width="1.5"/></svg>Robust SMS Interoperability</li>
    <li><svg width="14" height="14" viewBox="0 0 14 14"><circle cx="7" cy="7" r="6" fill="none" stroke="#7ab929" stroke-width="1.5"/><path d="M4 7l2 2 4-4" fill="none" stroke="#7ab929" stroke-width="1.5"/></svg>Proprietary IP protocol</li>
  </ul>
  <div class="abs person-photo" role="img" aria-label="Young woman sitting cross-legged holding a smartphone"></div>
</section>

<section class="video">
  <h2 class="abs video-title">WATCH THE VIDEO<br>LEARN MORE</h2>
  <p class="abs video-copy">Lorem ipsum dolor sit amet, consectetur adipiscing elit. Tempora similique excepturi obcaecati, maiores nostrum esse illo in soluta at saepe perspiciatis eos</p>
  <a class="abs btn video-btn">Contact us</a>
  <div class="abs video-frame" role="img" aria-label="Video still: collage of people using mobile phones">
    <svg class="abs" style="left:209px;top:120px" width="100" height="100" viewBox="0 0 100 100"><circle cx="50" cy="50" r="46" fill="rgba(0,0,0,.25)" stroke="#fff" stroke-width="4"/><path d="M40 32l28 18-28 18z" fill="#fff"/></svg>
    <div class="abs video-bar">
      <div class="abs" style="left:0;top:0;width:100%;height:4px;background:#555"></div>
      <div class="abs" style="left:0;top:0;width:230px;height:4px;background:#d22"></div>
      <svg class="abs" style="left:12px;top:11px" width="14" height="14" viewBox="0 0 14 14"><path d="M2 1l10 6-10 6z" fill="#fff"/></svg>
    </div>
  </div>
</section>

<section class="partners">
  <div class="abs partner-mark" style="left:50px;width:140px"></div>
  <div class="abs partner-mark" style="left:300px;width:120px"></div>
  <div class="abs partner-mark" style="left:540px;width:70px;border-radius:50%;height:60px;top:72px"></div>
  <div class="abs partner-mark" style="left:730px;width:140px"></div>
  <div class="abs partner-mark" style="left:960px;width:200px"></div>
</section>

<section class="contact">
  <h2 class="section-title">Contact Us</h2>
  <div class="abs field" style="left:148px;top:189px;width:380px;height:53px">Name</div>
  <div class="abs field" style="left:148px;top:270px;width:380px;height:51px">E-mail</div>
  <div class="abs field" style="left:550px;top:189px;width:540px;height:125px">Message</div>
  <a class="abs btn submit-btn">Submit</a>
</section>

<footer class="site-footer">
  <p class="abs foot-label" style="left:110px;top:55px">Email Newsletters</p>
  <div class="abs news-input">Enter your email address</div>
  <div class="abs news-go"></div>
  <p class="abs copyright">2015 © Copyright</p>
  <div class="abs divider" style="left:462px"></div>
  <p class="abs foot-label" style="left:565px;top:55px">Follow us</p>
  <div class="abs social"><i></i><i></i><i></i><i></i></div>
  <div class="abs divider" style="left:760px"></div>
  <div class="abs foot-brand">Vortel mobile</div>
</footer>

</body>
</html>
```